E-Book/ Buch-Cover spannenden Liebesroman gesucht.
Zielgruppe
Ich bin Autorin und suche ein ansprechendes Cover für mein E-Book mit dem Titel:
' Gläserne Sehnsucht'. Es handelt sich um einen spannenden Liebesroman. Die emotionalen Ängste des Protagonisten, stehen neben den offensichtlichen Bedrohungen der Hauptfigur. Beide müssen ihren Weg zu einem Happyend finden. Da der Titel schon etwas „schreit“, sollte das Cover diesen Eindruck eventuell etwas abfedern.
Aufgabenstellung
Kein Kitsch, kein Schnulzencover, es handelt sich bei aller Dramatik trotzdem um einen Liebesroman. Keinen Thriller.

```html
<!DOCTYPE html>
<html lang="de">
<head>
<meta charset="utf-8">
<title>Gläserne Sehnsucht – Buchcover</title>
<link rel="stylesheet" href="https://fonts.googleapis.com/css2?family=Libre+Bodoni:wght@400;500&display=swap">
<style>
  :root {
    --stage: #e6e6e4;
    --sky-top: #1c2c30;
    --sky-mid: #3f6469;
    --sky-haze: #7f9a9c;
    --sky-glow: #b98a7e;
    --horizon: #c2563a;
    --ground: #0d0f10;
    --figure: #111416;
    --ember: #e0621f;
    --type: #ffffff;
  }
  * { margin: 0; padding: 0; box-sizing: border-box; }
  html, body {
    width: 1200px;
    height: 800px;
    overflow: hidden;
    background: var(--stage);
  }
  .stage {
    position: relative;
    width: 1200px;
    height: 800px;
  }
  .cover {
    position: absolute;
    left: 370px;
    top: 40px;
    width: 460px;
    height: 720px;
    overflow: hidden;
    background: var(--ground);
  }
  .cover-sky,
  .cover-figure {
    position: absolute;
  }
  .cover-sky { inset: 0; }
  .cover-figure {
    left: 90px;
    top: 300px;
    width: 220px;
    height: 400px;
  }
  .cover-sky svg,
  .cover-figure svg {
    display: block;
    width: 100%;
    height: 100%;
  }
  .title {
    position: absolute;
    left: 0;
    right: 0;
    top: 82px;
    color: var(--type);
    font-family: "Libre Bodoni", "Bodoni Moda", serif;
    font-weight: 400;
    line-height: 1;
  }
  .title-line-small {
    display: block;
    text-align: right;
    padding-right: 30px;
    font-size: 44px;
    letter-spacing: -0.5px;
  }
  .title-line-large {
    display: block;
    text-align: center;
    margin-top: -4px;
    font-size: 92px;
    letter-spacing: -2px;
  }
  .author {
    position: absolute;
    left: 0;
    right: 0;
    top: 596px;
    text-align: center;
    color: var(--type);
    font-family: "Libre Bodoni", "Bodoni Moda", serif;
    font-size: 38px;
    letter-spacing: -0.5px;
  }
</style>
</head>
<body>
  <main class="stage">
    <article class="cover">
      <div class="cover-sky" role="img" aria-label="Abendhimmel, der von dunklem Petrol in einen orangeroten Horizont und eine dunkle Landschaft übergeht">
        <svg viewBox="0 0 460 720" preserveAspectRatio="none" aria-hidden="true">
          <defs>
            <linearGradient id="sky" x1="0" y1="0" x2="0" y2="1">
              <stop offset="0" stop-color="var(--sky-top)"/>
              <stop offset="0.38" stop-color="var(--sky-mid)"/>
              <stop offset="0.58" stop-color="var(--sky-haze)"/>
              <stop offset="0.68" stop-color="var(--sky-glow)"/>
              <stop offset="0.74" stop-color="var(--horizon)"/>
              <stop offset="0.8" stop-color="var(--ground)"/>
              <stop offset="1" stop-color="var(--ground)"/>
            </linearGradient>
          </defs>
          <rect width="460" height="720" fill="url(#sky)"/>
        </svg>
      </div>

      <div class="cover-figure" role="img" aria-label="Fotografie: Silhouette einer Frau mit wehendem Haar vor dem Abendhimmel, darunter eine Spur leuchtend oranger Lichtpunkte">
        <svg viewBox="0 0 220 400" preserveAspectRatio="none" aria-hidden="true">
          <defs>
            <linearGradient id="figure-tone" x1="0" y1="0" x2="0" y2="1">
              <stop offset="0" stop-color="var(--figure)" stop-opacity="0"/>
              <stop offset="0.12" stop-color="var(--figure)" stop-opacity="0.85"/>
              <stop offset="0.6" stop-color="var(--figure)" stop-opacity="0.95"/>
              <stop offset="0.82" stop-color="var(--ember)" stop-opacity="0.45"/>
              <stop offset="1" stop-color="var(--ember)" stop-opacity="0"/>
            </linearGradient>
            <linearGradient id="figure-fade" x1="0" y1="0" x2="1" y2="0">
              <stop offset="0" stop-color="#fff" stop-opacity="0"/>
              <stop offset="0.3" stop-color="#fff" stop-opacity="1"/>
              <stop offset="0.7" stop-color="#fff" stop-opacity="1"/>
              <stop offset="1" stop-color="#fff" stop-opacity="0"/>
            </linearGradient>
            <mask id="figure-mask">
              <rect width="220" height="400" fill="url(#figure-fade)"/>
            </mask>
          </defs>
          <rect width="220" height="400" rx="40" fill="url(#figure-tone)" mask="url(#figure-mask)"/>
        </svg>
      </div>

      <h1 class="title">
        <span class="title-line-small">Gläserne</span>
        <span class="title-line-large">Sehnsucht</span>
      </h1>

      <p class="author">L.K. Sternfeld</p>
    </article>
  </main>
</body>
</html>
```